Capacity building in Resource Management

Need design of a business card (later to be completed by letterhead and webdesign in same fashion) for a professional who works in the field of capacity building of professionals in mostly developing countries in the field waste/resource management, waste prevention/reduction, cleaner production, stakeholders involvement, etc.
Info on business cards is to include provided logo, info in provided file and picture.

Industry/Entity Type

Business

Contact Information for Business Card

White background

Font styles to use
Sans Serif

Colors

Designer to choose colors to be used in the design.

```html
<!DOCTYPE html>
<html lang="en">
<head>
<meta charset="utf-8">
<title>terra-learn stationery</title>
<link href="https://fonts.googleapis.com/css2?family=Questrial&display=swap" rel="stylesheet">
<style>
  :root {
    --green: #4a8a35;
    --green-dark: #2f5d22;
    --green-soft: #7fae6a;
    --ink: #222222;
    --card-bg: #2b2b2b;
    --paper: #ffffff;
    --backdrop: #efefec;
    --flap: #e4e8ed;
    --window: #eceff2;
  }
  html, body { margin: 0; padding: 0; overflow: hidden; }
  body { width: 1200px; height: 1200px; background: var(--backdrop); font-family: "Questrial", sans-serif; }
  .canvas { position: relative; width: 1200px; height: 1200px; overflow: hidden; }
  .piece { position: absolute; display: block; box-shadow: 0 4px 14px rgba(0,0,0,.12); background: var(--paper); }
  .envelope-front { left: 60px; top: 60px; width: 540px; height: 242px; }
  .envelope-back { left: 640px; top: 60px; width: 500px; height: 225px; }
  .cover { left: 60px; top: 360px; width: 468px; height: 582px; }
  .brochure { left: 568px; top: 360px; width: 246px; height: 574px; }
  .card-one { left: 860px; top: 360px; width: 280px; height: 166px; }
  .card-two { left: 860px; top: 560px; width: 280px; height: 166px; }
  svg text { font-family: "Questrial", sans-serif; }
  .brand { fill: var(--green); }
  .owner-name { fill: var(--ink); }
  .card-name { fill: #ffffff; }
  .card-line { fill: #e6e6e6; }
  .card-icon { fill: var(--green); }
</style>
</head>
<body>
<div class="canvas">

  <!-- Window envelope -->
  <svg class="piece envelope-front" viewBox="0 0 450 202" preserveAspectRatio="none">
    <defs>
      <linearGradient id="accent-env" x1="0" y1="0" x2="0" y2="1">
        <stop offset="0" stop-color="var(--green-soft)"/>
        <stop offset="1" stop-color="var(--green)"/>
      </linearGradient>
    </defs>
    <rect width="450" height="202" fill="var(--paper)"/>
    <rect x="0" y="28" width="36" height="68" fill="url(#accent-env)" role="img" aria-label="Green decorative accent graphic"/>
    <text class="brand" x="444" y="55" text-anchor="end" font-size="20">terra-learn</text>
    <rect x="262" y="113" width="150" height="60" rx="4" fill="var(--window)" stroke="#d8dbe0"/>
  </svg>

  <!-- Envelope back -->
  <svg class="piece envelope-back" viewBox="0 0 450 202" preserveAspectRatio="none">
    <rect width="450" height="202" fill="var(--paper)"/>
    <polygon points="0,0 450,0 450,50 440,80 10,80 0,50" fill="var(--flap)"/>
  </svg>

  <!-- Notebook cover -->
  <svg class="piece cover" viewBox="0 0 390 485" preserveAspectRatio="none">
    <defs>
      <linearGradient id="accent-cover" x1="0" y1="0" x2="0" y2="1">
        <stop offset="0" stop-color="var(--green-soft)"/>
        <stop offset="1" stop-color="var(--green)"/>
      </linearGradient>
    </defs>
    <rect width="390" height="485" fill="var(--paper)"/>
    <rect x="0" y="0" width="10" height="485" fill="#f1f1f1"/>
    <text class="brand" x="315" y="135" text-anchor="end" font-size="30">terra-learn</text>
    <rect x="15" y="200" width="160" height="195" fill="url(#accent-cover)" role="img" aria-label="Green decorative accent graphic"/>
    <text class="owner-name" x="215" y="410" text-anchor="middle" font-size="20">Joren Vaalbeek</text>
  </svg>

  <!-- Brochure -->
  <svg class="piece brochure" viewBox="0 0 205 478" preserveAspectRatio="none">
    <defs>
      <linearGradient id="accent-brochure" x1="0" y1="0" x2="0" y2="1">
        <stop offset="0" stop-color="var(--green-soft)"/>
        <stop offset="1" stop-color="var(--green)"/>
      </linearGradient>
    </defs>
    <rect width="205" height="478" fill="var(--paper)"/>
    <text class="brand" x="158" y="118" text-anchor="end" font-size="17">terra-learn</text>
    <rect x="0" y="185" width="128" height="175" fill="url(#accent-brochure)" role="img" aria-label="Green decorative accent graphic"/>
    <text class="owner-name" x="98" y="395" text-anchor="middle" font-size="22">TERRA</text>
    <text class="owner-name" x="98" y="425" text-anchor="middle" font-size="22">BRONCHURE</text>
  </svg>

  <!-- Business cards -->
  <svg class="piece card-one" viewBox="0 0 177 105" preserveAspectRatio="none">
    <rect width="177" height="105" fill="var(--card-bg)"/>
    <text class="brand" x="173" y="22" text-anchor="end" font-size="12">terra-learn</text>
    <circle cx="40" cy="52" r="24" fill="#ffffff"/>
    <circle cx="40" cy="52" r="22" fill="#8a8f95" role="img" aria-label="Portrait photo of Joren Vaalbeek"/>
    <text class="card-name" x="40" y="88" text-anchor="middle" font-size="6.5">JOREN VAALBEEK</text>
    <rect x="80" y="38" width="0.5" height="58" fill="#555"/>
    <g font-size="3.8">
      <circle class="card-icon" cx="84" cy="42" r="1.3"/><text class="card-line" x="87" y="43.3">+49 1500 000 1234</text>
      <circle class="card-icon" cx="84" cy="48" r="1.3"/><text class="card-line" x="87" y="49.3">www.terra-learn.example</text>
      <circle class="card-icon" cx="84" cy="54" r="1.3"/><text class="card-line" x="87" y="55.3">joren.vaalbeek@terra-learn.example</text>
      <circle class="card-icon" cx="84" cy="60" r="1.3"/><text class="card-line" x="87" y="61.3">Lindenweg 12 10117 Berlin Germany</text>
      <circle class="card-icon" cx="84" cy="68" r="1.3"/><text class="card-line" x="87" y="69.3">vaalbeek88</text>
      <circle class="card-icon" cx="84" cy="74" r="1.3"/><text class="card-line" x="87" y="75.3">@jorenvaalbeek</text>
      <circle class="card-icon" cx="84" cy="80" r="1.3"/><text class="card-line" x="87" y="81.3">Joren Vaalbeek</text>
      <circle class="card-icon" cx="84" cy="86" r="1.3"/><text class="card-line" x="87" y="87.3">+49 1500 000 1234 (messenger)</text>
    </g>
    <rect x="0" y="100" width="177" height="5" fill="var(--green)"/>
  </svg>

  <svg class="piece card-two" viewBox="0 0 177 105" preserveAspectRatio="none">
    <rect width="177" height="105" fill="var(--card-bg)"/>
    <text class="brand" x="173" y="22" text-anchor="end" font-size="12">terra-learn</text>
    <circle cx="40" cy="52" r="24" fill="#ffffff"/>
    <circle cx="40" cy="52" r="22" fill="#8a8f95" role="img" aria-label="Portrait photo of Joren Vaalbeek"/>
    <text class="card-name" x="40" y="88" text-anchor="middle" font-size="6.5">JOREN VAALBEEK</text>
    <rect x="80" y="38" width="0.5" height="58" fill="#555"/>
    <g font-size="3.8">
      <circle class="card-icon" cx="84" cy="42" r="1.3"/><text class="card-line" x="87" y="43.3">+49 1500 000 1234</text>
      <circle class="card-icon" cx="84" cy="48" r="1.3"/><text class="card-line" x="87" y="49.3">www.terra-learn.example</text>
      <circle class="card-icon" cx="84" cy="54" r="1.3"/><text class="card-line" x="87" y="55.3">joren.vaalbeek@terra-learn.example</text>
      <circle class="card-icon" cx="84" cy="60" r="1.3"/><text class="card-line" x="87" y="61.3">Lindenweg 12 10117 Berlin Germany</text>
      <circle class="card-icon" cx="84" cy="68" r="1.3"/><text class="card-line" x="87" y="69.3">vaalbeek88</text>
      <circle class="card-icon" cx="84" cy="74" r="1.3"/><text class="card-line" x="87" y="75.3">@jorenvaalbeek</text>
      <circle class="card-icon" cx="84" cy="80" r="1.3"/><text class="card-line" x="87" y="81.3">Joren Vaalbeek</text>
      <circle class="card-icon" cx="84" cy="86" r="1.3"/><text class="card-line" x="87" y="87.3">+49 1500 000 1234 (messenger)</text>
    </g>
    <rect x="0" y="100" width="177" height="5" fill="var(--green)"/>
  </svg>

</div>
</body>
</html>
```